Email Signature & Social Cover Design – Birchlane Study Centre

I’m looking for a clean, professional email signature and a matching Social cover photo for my tutoring business, Birchlane Study Centre.
The email signature needs to display properly across Outlook and iPhone without the image appearing as an attachment. It should include my logo and contact details and have a friendly but professional look suitable for an education business.
Details to include:
Moira Dunholt
Director & Lead Tutor
Birchlane Study Centre
hello@birchlanestudy.co.uk
www.birchlanestudy.co.uk
01632 418736
The Social cover should match the branding, feel professional and welcoming, and be optimised for desktop and mobile.

```html
<!DOCTYPE html>
<html lang="en">
<head>
<meta charset="utf-8">
<title>Birchlane Study Centre – Email Signature &amp; Social Cover</title>
<link href="https://fonts.googleapis.com/css2?family=Poppins:wght@300;400;500;600;700&family=Roboto:wght@400;500;700&display=swap" rel="stylesheet">
<style>
  :root{
    --bg:#2f2e30;
    --green:#57d07c;
    --lime:#c6f65e;
    --ink:#1b1b1e;
    --strip:#1f1f22;
    --paper:#ffffff;
    --stripe:#f3f3f3;
    --label:#7a7a7a;
    --ui-blue:#1877f2;
    --ui-grey:#e4e6eb;
    --ui-feed:#eceef1;
    --ui-text:#050505;
    --ui-muted:#65676b;
  }
  *{box-sizing:border-box;margin:0;padding:0}
  html,body{width:1200px;height:1053px;overflow:hidden;background:var(--bg)}
  .stage{position:absolute;left:0;top:0;width:2044px;height:1794px;transform:scale(0.58708);transform-origin:0 0;font-family:'Poppins',sans-serif}
  .section-label{position:absolute;left:0;width:2044px;text-align:center;font-weight:300;font-size:21px;color:var(--label);letter-spacing:.5px}
  .section-label--signature{top:108px}
  .section-label--cover{top:728px}
  .signature{position:absolute;left:92px;top:171px;filter:drop-shadow(0 6px 10px rgba(0,0,0,.35))}
  .brand-name{font-family:'Poppins',sans-serif;font-weight:700;fill:var(--green)}
  .person-name{font-family:'Poppins',sans-serif;font-weight:600;fill:var(--ink)}
  .person-role{font-family:'Poppins',sans-serif;font-weight:400;fill:var(--ink)}
  .contact-label{font-family:'Poppins',sans-serif;font-weight:600;fill:var(--ink)}
  .contact-value{font-family:'Poppins',sans-serif;font-weight:400;fill:var(--ink)}
  .handle{font-family:'Poppins',sans-serif;font-weight:400;fill:#fff}

  .page{position:absolute;left:92px;top:786px;width:1854px;height:927px;background:var(--paper);overflow:hidden;font-family:'Roboto',sans-serif;color:var(--ui-text)}
  .topbar{position:absolute;left:0;top:0;width:100%;height:54px;background:#fff;border-bottom:1px solid #e6e6e6}
  .topbar__mark{position:absolute;left:15px;top:7px;width:38px;height:38px;border-radius:50%;background:var(--ui-blue)}
  .topbar__search{position:absolute;left:61px;top:8px;width:272px;height:37px;border-radius:19px;background:#f0f2f5;font-size:15px;color:var(--ui-muted);line-height:37px;padding-left:36px}
  .topbar__search svg{position:absolute;left:12px;top:10px}
  .topbar__nav{position:absolute;left:0;top:0}
  .topbar__tools{position:absolute;right:6px;top:7px;display:flex;gap:9px}
  .topbar__tools span{width:38px;height:38px;border-radius:50%;background:var(--ui-grey)}
  .cover-side{position:absolute;top:54px;height:625px;background:linear-gradient(180deg,#cfd1d4 0%,#e9eaec 55%,#f4f5f6 100%)}
  .cover-side--left{left:0;width:322px}
  .cover-side--right{left:1538px;width:316px}
  .cover{position:absolute;left:322px;top:54px}
  .feed-bg{position:absolute;left:0;top:679px;width:100%;height:248px;background:var(--ui-feed)}
  .avatar{position:absolute;left:355px;top:438px;width:166px;height:166px;border-radius:50%;background:var(--green);border:5px solid var(--ui-blue);box-shadow:inset 0 0 0 5px #fff;display:flex;flex-direction:column;align-items:center;justify-content:center}
  .avatar span{font-family:'Poppins',sans-serif;font-weight:700;color:#fff;font-size:19px;line-height:21px}
  .page-title{position:absolute;left:540px;top:524px;font-size:30px;font-weight:700;display:flex;align-items:center;gap:10px}
  .page-title i{display:inline-block;width:17px;height:17px;border-radius:50%;background:var(--ui-blue);position:relative}
  .page-title i::after{content:"";position:absolute;left:5px;top:3px;width:4px;height:8px;border:solid #fff;border-width:0 2px 2px 0;transform:rotate(45deg)}
  .page-stats{position:absolute;left:540px;top:568px;font-size:17px;color:var(--ui-muted)}
  .actions{position:absolute;left:1184px;top:554px;display:flex;gap:7px}
  .btn{height:33px;border-radius:6px;font-size:15px;font-weight:500;display:flex;align-items:center;gap:7px;padding:0 12px;background:var(--ui-grey);color:var(--ui-text)}
  .btn--primary{background:var(--ui-blue);color:#fff}
  .btn b{display:inline-block;width:15px;height:15px;border-radius:3px;background:var(--ui-text)}
  .btn--primary b{border-radius:50%;background:#fff}
  .btn--search b{background:none;border:2px solid var(--ui-text);border-radius:50%;width:13px;height:13px}
  .rule{position:absolute;left:355px;top:619px;width:1152px;height:1px;background:#ced0d4}
  .tabs{position:absolute;left:355px;top:640px;display:flex;font-size:15px;font-weight:500;color:var(--ui-muted)}
  .tabs span{padding:0 16px;height:38px}
  .tabs .is-active{color:var(--ui-blue);border-bottom:3px solid var(--ui-blue);height:38px}
  .more-dots{position:absolute;left:1461px;top:632px;width:46px;height:34px;border-radius:6px;background:var(--ui-grey);text-align:center;font-weight:700;line-height:26px;font-size:18px}
  .card{position:absolute;background:#fff;border-radius:8px;box-shadow:0 1px 2px rgba(0,0,0,.12)}
  .card--intro{left:356px;top:696px;width:474px;height:220px;padding:14px 15px}
  .card h3{font-size:21px;font-weight:700}
  .intro__bio{font-size:15px;text-align:center;margin-top:12px;padding-bottom:12px;border-bottom:1px solid #ced0d4}
  .intro__row{display:flex;align-items:center;gap:12px;font-size:15px;margin-top:19px}
  .intro__row i{width:19px;height:19px;border-radius:50%;background:#8a8d91;display:inline-block}
  .intro__row a{color:#216fdb;text-decoration:none}
  .card--posts-head{left:846px;top:696px;width:661px;height:46px;padding:10px 15px;display:flex;justify-content:space-between;align-items:center}
  .filters{background:var(--ui-grey);border-radius:6px;font-size:14px;font-weight:500;padding:6px 12px}
  .card--post{left:846px;top:759px;width:661px;height:180px;padding:12px 16px}
  .post__head{display:flex;gap:11px;align-items:center}
  .post__avatar{width:38px;height:38px;border-radius:50%;background:#d8d9db}
  .post__name{font-size:15px;font-weight:700;line-height:17px}
  .post__date{font-size:12px;color:var(--ui-muted)}
  .post__dots{position:absolute;right:24px;top:12px;font-weight:700;font-size:18px}
  .post__body{font-size:14.5px;line-height:19.5px;margin-top:14px}
  .post__body a{color:#216fdb;text-decoration:none}
  .post__media{position:absolute;left:2px;right:2px;top:135px;height:45px;background:#e3e3e3}
</style>
</head>
<body>
<svg width="0" height="0" style="position:absolute" aria-hidden="true">
  <defs>
    <symbol id="ico-phone" viewBox="0 0 24 24"><path d="M7.5 4h3l1.4 3.8-2 1.4a10 10 0 0 0 4.9 4.9l1.4-2 3.8 1.4v3a2 2 0 0 1-2 2A15.5 15.5 0 0 1 5.5 6a2 2 0 0 1 2-2z" fill="#fff"/></symbol>
    <symbol id="ico-mail" viewBox="0 0 24 24"><rect x="4" y="6" width="16" height="12" rx="2" fill="#fff"/><path d="M4.5 7l7.5 6 7.5-6" fill="none" stroke="#57d07c" stroke-width="1.8"/></symbol>
    <symbol id="ico-globe" viewBox="0 0 24 24"><circle cx="12" cy="12" r="8" fill="none" stroke="#fff" stroke-width="2"/><ellipse cx="12" cy="12" rx="3.5" ry="8" fill="none" stroke="#fff" stroke-width="1.6"/><path d="M4 12h16" stroke="#fff" stroke-width="1.6"/></symbol>
    <linearGradient id="photo-tone" x1="0" y1="0" x2="1" y2="1">
      <stop offset="0" stop-color="#d9cdbd"/><stop offset=".5" stop-color="#a28a72"/><stop offset="1" stop-color="#3b2f29"/>
    </linearGradient>
  </defs>
</svg>

<div class="stage">
  <p class="section-label section-label--signature">Email Signature</p>

  <svg class="signature" width="1858" height="471" viewBox="0 0 1858 471">
    <rect width="1858" height="471" fill="var(--paper)"/>
    <g class="signature__stripes" fill="var(--stripe)">
      <rect x="560" y="-260" width="70" height="620" rx="35" transform="rotate(45 595 50)"/>
      <rect x="1180" y="160" width="80" height="620" rx="40" transform="rotate(45 1220 470)"/>
      <rect x="1330" y="150" width="70" height="620" rx="35" transform="rotate(45 1365 460)"/>
      <rect x="1460" y="190" width="60" height="520" rx="30" transform="rotate(45 1490 450)"/>
    </g>
    <rect class="signature__strip" width="93" height="471" fill="var(--strip)"/>
    <rect x="47" y="29" width="122" height="121" fill="var(--green)"/>
    <path d="M0 0h13v92h93V0h20v107H0z" fill="var(--lime)"/>
    <text class="handle" font-size="15" transform="translate(49 272) rotate(-90)">@username</text>
    <g fill="#fff"><circle cx="45" cy="293" r="10"/><circle cx="45" cy="324" r="10"/><circle cx="45" cy="354" r="10"/><circle cx="45" cy="384" r="10"/></g>
    <circle cx="95" cy="369" r="24" fill="var(--lime)"/>

    <g class="brand-lockup" text-anchor="middle">
      <text class="brand-name" x="424" y="146" font-size="58">Birchlane</text>
      <text class="brand-name" x="424" y="212" font-size="58">Study</text>
      <text class="brand-name" x="424" y="278" font-size="58">Centre</text>
      <text class="person-name" x="424" y="334" font-size="26">Moira Dunholt</text>
      <text class="person-role" x="424" y="364" font-size="18">Director &amp; Lead Tutor</text>
    </g>
    <rect x="699" y="84" width="3" height="298" fill="var(--ink)"/>

    <g class="contacts">
      <circle cx="800" cy="114" r="19" fill="var(--green)"/><use href="#ico-phone" x="788" y="102" width="24" height="24"/>
      <text class="contact-label" x="838" y="124" font-size="28">Phone</text>
      <text class="contact-value" x="838" y="158" font-size="22">01632 418736</text>
      <circle cx="800" cy="227" r="19" fill="var(--green)"/><use href="#ico-mail" x="788" y="215" width="24" height="24"/>
      <text class="contact-label" x="838" y="233" font-size="28">Email</text>
      <text class="contact-value" x="838" y="267" font-size="22">hello@birchlanestudy.co.uk</text>
      <circle cx="800" cy="329" r="19" fill="var(--green)"/><use href="#ico-globe" x="788" y="317" width="24" height="24"/>
      <text class="contact-label" x="838" y="338" font-size="28">Website</text>
      <text class="contact-value" x="838" y="368" font-size="22">www.birchlanestudy.co.uk</text>
    </g>

    <path d="M1722 0H1858V175L1700 428L1628 350Z" fill="var(--green)"/>
    <rect x="-190" y="-190" width="380" height="380" rx="72" fill="#fff" transform="translate(1535 122) rotate(45)"/>
    <rect role="img" aria-label="Photo of a smiling tutor and student working together at a laptop" x="-175" y="-175" width="350" height="350" rx="62" fill="url(#photo-tone)" transform="translate(1535 122) rotate(45)"/>
    <path d="M1723 322L1858 180V442Z" fill="var(--lime)"/>
    <circle cx="1668" cy="389" r="40" fill="none" stroke="var(--ink)" stroke-width="5"/>
  </svg>

  <p class="section-label section-label--cover">Social Cover</p>

  <div class="page">
    <div class="topbar">
      <span class="topbar__mark"></span>
      <div class="topbar__search"><svg width="16" height="16" viewBox="0 0 16 16"><circle cx="7" cy="7" r="5" fill="none" stroke="#65676b" stroke-width="2"/><path d="M11 11l4 4" stroke="#65676b" stroke-width="2"/></svg>Search Social</div>
      <svg class="topbar__nav" width="1854" height="54" fill="none" stroke="#65676b" stroke-width="2">
        <path d="M652 28l12-11 12 11v10h-24z"/>
        <circle cx="792" cy="21" r="5"/><circle cx="805" cy="21" r="4"/><path d="M782 36c0-6 5-9 10-9s10 3 10 9zM803 28c5 0 9 2 9 7"/>
        <rect x="920" y="18" width="22" height="18" rx="3"/><path d="M928 23l7 4-7 4z" fill="#65676b"/>
        <path d="M1054 20h22l2 7h-26zM1056 27v11h18V27M1062 38v-6h6v6"/>
        <rect x="1188" y="17" width="20" height="21" rx="2"/><path d="M1193 24h10M1193 24v9"/>
      </svg>
      <svg style="position:absolute;left:938px;top:6px" width="26" height="18"><rect width="26" height="18" rx="9" fill="#e41e3f"/><text x="13" y="13" text-anchor="middle" font-size="11" font-family="Roboto,sans-serif" font-weight="700" fill="#fff">9+</text></svg>
      <div class="topbar__tools"><span></span><span></span><span></span><span></span></div>
    </div>

    <div class="cover-side cover-side--left"></div>
    <div class="cover-side cover-side--right"></div>

    <svg class="cover" width="1216" height="450" viewBox="0 0 1216 450">
      <rect width="1216" height="450" fill="var(--paper)"/>
      <g fill="var(--stripe)">
        <rect x="330" y="-240" width="60" height="560" rx="30" transform="rotate(45 360 40)"/>
        <rect x="800" y="160" width="70" height="520" rx="35" transform="rotate(45 835 420)"/>
        <rect x="920" y="170" width="60" height="480" rx="30" transform="rotate(45 950 410)"/>
      </g>
      <rect width="88" height="450" fill="var(--strip)"/>
      <rect x="45" y="26" width="116" height="116" fill="var(--green)"/>
      <path d="M0 0h13v88h93V0h13v100H0z" fill="var(--lime)"/>
      <text class="handle" font-size="13" transform="translate(47 258) rotate(-90)">@username</text>
      <g fill="#fff"><circle cx="43" cy="279" r="9"/><circle cx="43" cy="308" r="9"/><circle cx="43" cy="337" r="9"/><circle cx="43" cy="366" r="9"/></g>
      <circle cx="90" cy="350" r="23" fill="var(--lime)"/>

      <g text-anchor="middle">
        <text class="brand-name" x="319" y="180" font-size="46">Birchlane</text>
        <text class="brand-name" x="319" y="236" font-size="46">Study</text>
        <text class="brand-name" x="319" y="292" font-size="46">Centre</text>
      </g>
      <rect x="508" y="120" width="2" height="205" fill="var(--ink)"/>

      <circle cx="578" cy="140" r="13" fill="var(--green)"/><use href="#ico-phone" x="570" y="132" width="16" height="16"/>
      <text class="contact-label" x="604" y="148" font-size="20">Phone</text>
      <text class="contact-value" x="604" y="170" font-size="16">01632 418736</text>
      <circle cx="578" cy="217" r="13" fill="var(--green)"/><use href="#ico-mail" x="570" y="209" width="16" height="16"/>
      <text class="contact-label" x="604" y="224" font-size="20">Email</text>
      <text class="contact-value" x="604" y="246" font-size="16">hello@birchlanestudy.co.uk</text>
      <circle cx="578" cy="289" r="13" fill="var(--green)"/><use href="#ico-globe" x="570" y="281" width="16" height="16"/>
      <text class="contact-label" x="604" y="296" font-size="20">Website</text>
      <text class="contact-value" x="604" y="315" font-size="16">www.birchlanestudy.co.uk</text>

      <path d="M1111 0H1216V355L1135 415L1050 332Z" fill="var(--green)"/>
      <rect x="-155" y="-155" width="310" height="310" rx="60" fill="#fff" transform="translate(996 130) rotate(45)"/>
      <rect role="img" aria-label="Photo of a smiling tutor and student working together at a laptop" x="-143" y="-143" width="286" height="286" rx="52" fill="url(#photo-tone)" transform="translate(996 130) rotate(45)"/>
      <path d="M1146 282L1216 210V355Z" fill="var(--lime)"/>
      <circle cx="1090" cy="369" r="40" fill="none" stroke="var(--ink)" stroke-width="5"/>
    </svg>

    <div class="feed-bg"></div>

    <div class="avatar"><span>Birchlane</span><span>Study</span><span>Centre</span></div>
    <div class="page-title">Your Text <i></i></div>
    <div class="page-stats">7.7M followers . 70 following</div>
    <div class="actions">
      <span class="btn"><b></b>Following</span>
      <span class="btn btn--primary"><b></b>Message</span>
      <span class="btn btn--search"><b></b>Search</span>
    </div>
    <div class="rule"></div>
    <div class="tabs">
      <span class="is-active">Posts</span><span>About</span><span>Mentions</span><span>Reviews</span><span>Followers</span><span>Photos</span><span>More ▾</span>
    </div>
    <div class="more-dots">···</div>

    <section class="card card--intro">
      <h3>Intro</h3>
      <p class="intro__bio">The ONLY official page managed by Juniper Lane.</p>
      <p class="intro__row"><i></i><span><strong>Page</strong> . Jounalist</span></p>
      <p class="intro__row"><i></i><a>juniperlane.com/lane</a></p>
      <p class="intro__row"><i></i><span>Rating . 5.0 (4,701)</span></p>
    </section>

    <section class="card card--posts-head">
      <h3>Posts</h3><span class="filters">⚟ Filters</span>
    </section>

    <article class="card card--post">
      <div class="post__head">
        <span class="post__avatar"></span>
        <div><p class="post__name">Birchlane Study Centre</p><p class="post__date">18 January 2022 · ◍</p></div>
      </div>
      <span class="post__dots">···</span>
      <p class="post__body">Lorem ipsum dolor sit amet, consectetur adipiscing elit, sed do eiusmod tempor incididunt ut labore et dolore magna aliqua. Quis ipsum suspendisse ultrices gravida. Risus commodo viverra maecenas accumsan lacus vel facilisis. <a>#food</a></p>
      <div class="post__media"></div>
    </article>
  </div>
</div>
</body>
</html>
```